MindHarbor Powerpoint Presentation Template

I am looking for a PowerPoint template that I can use for my presentations. I have attached a copy of my logo that your community has previously designed for me. My presentations are typically visual with very little text being used.
I have included my current presentation style using my old corporate colours (they are very different). There is one condition, the template must not have a white background as this detracts the focus of the crowd away from the presenter (which defeats the purpose of having a presenter in the first place).
Thank you for your time in coming up with a design!
Liam
Look and feel
Each slider illustrates characteristics of the customer's brand and the style your logo design should communicate.

```html
<!DOCTYPE html>
<html lang="en">
<head>
<meta charset="utf-8">
<title>MindHarbor Presentation Template</title>
<link href="https://fonts.googleapis.com/css2?family=Poppins:wght@300;400;600;700&family=Open+Sans:wght@400;700&family=Montserrat:wght@800&display=swap" rel="stylesheet">
<style>
  :root{
    --page:#e4e5e7;
    --blue:#1696ee;
    --blue-deep:#0e6cb3;
    --ink:#0a0405;
    --night:#1c1c1e;
    --white:#ffffff;
  }
  *{margin:0;padding:0;box-sizing:border-box}
  html,body{width:1200px;height:3288px;overflow:hidden;background:var(--page)}
  body{position:relative;font-family:"Open Sans",Arial,sans-serif;color:var(--white)}
  .slide{position:absolute;left:106px;width:1002px;height:563px;overflow:hidden}
  .abs{position:absolute}
  .brand{display:flex;align-items:center;gap:12px;font-family:"Poppins",Arial,sans-serif;font-weight:600;color:var(--white);white-space:nowrap}
  .brand .dot{border-radius:50%;background:var(--blue);flex:none}

  /* slide 1 */
  .s-welcome{top:96px;background:radial-gradient(ellipse at 60% 45%,#3a3634 0%,#221f1e 55%,#141313 100%)}
  .s-welcome .brand{left:0;right:0;top:142px;justify-content:center;font-size:44px}
  .s-welcome .brand .dot{width:26px;height:26px}
  .welcome-kicker{left:0;right:0;top:292px;text-align:center;font:700 36px "Poppins",Arial,sans-serif}
  .welcome-title{left:0;right:0;top:338px;text-align:center;font:700 62px "Poppins",Arial,sans-serif;letter-spacing:1px}

  /* slide 2 */
  .s-safety{top:708px;background:var(--blue)}
  .s-safety svg{position:absolute;inset:0}
  .s-safety .brand{left:0;width:452px;top:155px;justify-content:center;font-size:34px}
  .s-safety .brand .dot{width:20px;height:20px;background:var(--white)}
  .safety-title{left:0;width:452px;top:272px;text-align:center;font:700 25px "Open Sans",Arial,sans-serif}
  .safety-text{left:0;width:452px;top:329px;text-align:center;font-size:20px;line-height:27px}

  /* slide 3 */
  .s-pillars{top:1333px;background:var(--blue)}
  .pillars-side{left:0;top:0;width:479px;height:563px;background:var(--ink)}
  .s-pillars .brand{left:0;width:410px;top:134px;justify-content:center;font-size:33px}
  .s-pillars .brand .dot{width:20px;height:20px}
  .pillars-intro{left:65px;width:280px;top:254px;text-align:center;font-size:16px;line-height:23px}
  .pillar-badge{width:120px;height:120px;border-radius:50%;background:var(--ink);display:flex;align-items:center;justify-content:center}
  .pillar-badge span{width:100px;height:100px;border-radius:50%;background:var(--blue);display:flex;align-items:center;justify-content:center}
  .pillar h3{font:700 20px "Open Sans",Arial,sans-serif;margin-bottom:9px}
  .pillar p{font-size:14px;line-height:19px;width:360px}
  .pillar{left:565px}

  /* slide 4 */
  .s-grid{top:1970px;background:var(--blue)}
  .s-grid svg.wave{position:absolute;left:0;top:0}
  .grid-logo{left:18px;top:15px;width:198px;height:128px;background:var(--ink);display:flex;align-items:center;justify-content:center}
  .grid-logo .brand{font-size:27px;gap:8px}
  .grid-logo .dot{width:16px;height:16px}
  .grid-headline{left:585px;top:34px;width:380px;font:300 27px/37px "Poppins",Arial,sans-serif}
  .feature-photo{width:128px;height:128px;border-radius:50%}
  .feature h3{font:700 14px "Open Sans",Arial,sans-serif;letter-spacing:1px;margin-bottom:12px}
  .feature p{font-size:13.5px;line-height:19px;width:215px}

  /* slide 5 */
  .s-closing{top:2589px;background:#000}
  .closing-photo{left:525px;top:-11px;width:500px;height:500px;border-radius:50%;background:radial-gradient(circle at 50% 45%,#f3a23d 0%,#b8743a 14%,#4a4340 38%,#2e2c2c 70%,#222 100%)}
  .closing-title{left:43px;top:48px;font:800 25px/37px "Montserrat",Arial,sans-serif;letter-spacing:1.5px}
  .closing-text{left:43px;top:179px;width:410px;font-size:19px;line-height:26px}
  .s-closing .brand{left:43px;top:460px;font-size:33px}
  .s-closing .brand .dot{width:20px;height:20px}
</style>
</head>
<body>

<section class="slide s-welcome" role="img" aria-label="Dimmed photo of a group session with people raising their hands">
  <div class="abs brand"><span>MindHarbor</span><span class="dot"></span></div>
  <div class="abs welcome-kicker">WELCOME TO</div>
  <div class="abs welcome-title">MINDHARBOR</div>
</section>

<section class="slide s-safety">
  <svg width="1002" height="563" viewBox="0 0 1002 563">
    <polygon points="447,0 1002,0 1002,563 564,563" fill="var(--blue-deep)"/>
    <polygon points="457,0 1002,0 1002,563 533+0,563" fill="#9aa3b0" role="img" aria-label="Photo of a counsellor with a clipboard listening to a client"/>
  </svg>
  <div class="abs brand"><span>MindHarbor</span><span class="dot"></span></div>
  <h2 class="abs safety-title">PSYCHOLOGICAL SAFETY</h2>
  <p class="abs safety-text">The essential ingredient to every<br>great workplace culture and<br>high performing team.</p>
</section>

<section class="slide s-pillars">
  <div class="abs pillars-side"></div>
  <div class="abs brand"><span>MindHarbor</span><span class="dot"></span></div>
  <p class="abs pillars-intro">There are many variations of passages of Lorem Ipsum available, but the majority have suffered alteration in some form, by injected humour, or randomised words which don't look even slightly believable.</p>

  <div class="abs pillar-badge" style="left:424px;top:54px"><span>
    <svg width="52" height="52" viewBox="0 0 52 52" fill="#fff"><circle cx="26" cy="14" r="5"/><path d="M26 21c-4 0-6 4-6 9l4 2v16h4V32l4-2c0-5-2-9-6-9z"/><ellipse cx="12" cy="18" rx="4" ry="7" transform="rotate(-35 12 18)"/><ellipse cx="40" cy="18" rx="4" ry="7" transform="rotate(35 40 18)"/><ellipse cx="26" cy="4" rx="3" ry="4"/></svg>
  </span></div>
  <div class="abs pillar-badge" style="left:424px;top:221px"><span>
    <svg width="60" height="40" viewBox="0 0 60 40" fill="#fff"><rect x="0" y="6" width="8" height="22" rx="1"/><rect x="52" y="6" width="8" height="22" rx="1"/><path d="M10 9l12-3 8 4 8-4 12 3v16l-6 4-12 8-6-3-6-6-10-3z"/><path d="M28 12l-8 6 4 3 8-5" fill="var(--blue)"/></svg>
  </span></div>
  <div class="abs pillar-badge" style="left:424px;top:389px"><span>
    <svg width="48" height="48" viewBox="0 0 48 48" fill="#fff"><path d="M4 8h10a4 4 0 1 1 8 0h10v10a4 4 0 1 1 0 8v10H22a4 4 0 1 0-8 0H4V26a4 4 0 1 0 0-8z"/><path d="M30 30l4 14 3-5 5 5 3-3-5-5 5-3z" stroke="var(--blue)" stroke-width="1.5"/></svg>
  </span></div>

  <div class="abs pillar" style="top:62px"><h3>Lorem Ipsum is simply</h3><p>There are many variations of passages of Lorem Ipsum available, but the majority have suffered alteration in some form, by injected humour, or randomised words which don't look even slightly believable.</p></div>
  <div class="abs pillar" style="top:229px"><h3>t is a long established</h3><p>There are many variations of passages of Lorem Ipsum available, but the majority have suffered alteration in some form, by injected humour, or randomised words which don't look even slightly believable.</p></div>
  <div class="abs pillar" style="top:398px"><h3>Contrary to popular</h3><p>There are many variations of passages of Lorem Ipsum available, but the majority have suffered alteration in some form, by injected humour, or randomised words which don't look even slightly believable.</p></div>
</section>

<section class="slide s-grid">
  <svg class="wave" width="1002" height="563" viewBox="0 0 1002 563">
    <path d="M0 0H1002V160C900 185 760 198 560 196C360 194 200 170 0 178Z" fill="var(--night)" role="img" aria-label="Dimmed photo of a workshop audience"/>
  </svg>
  <div class="abs grid-logo"><div class="brand"><span>MindHarbor</span><span class="dot"></span></div></div>
  <p class="abs grid-headline">There are many variations of passages of Lorem Ipsum available</p>

  <div class="abs feature-photo" style="left:32px;top:232px;background:radial-gradient(circle at 45% 50%,#f2efe9,#c9b7a0 60%,#8b6f55)" role="img" aria-label="Photo of hands writing notes on a clipboard"></div>
  <div class="abs feature" style="left:183px;top:238px"><h3>LOREM IPSUM IS SIMPLY</h3><p>It is a long established fact that a reader will be distracted by the readable content of a page when looking at its layout.</p></div>

  <div class="abs feature-photo" style="left:564px;top:232px;background:radial-gradient(circle at 50% 60%,#f0a050,#9a5a3a 40%,#2a2c3e 80%)" role="img" aria-label="Photo of a glowing brain above an open hand"></div>
  <div class="abs feature" style="left:714px;top:238px"><h3>LOREM IPSUM IS SIMPLY</h3><p>It is a long established fact that a reader will be distracted by the readable content of a page when looking at its layout.</p></div>

  <div class="abs feature-photo" style="left:32px;top:389px;background:radial-gradient(circle at 45% 40%,#5a5a5a,#2f2f2f 70%,#1e1e1e)" role="img" aria-label="Illustration of colourful blocks inside a head outline on a chalkboard"></div>
  <div class="abs feature" style="left:183px;top:395px"><h3>LOREM IPSUM IS SIMPLY</h3><p>It is a long established fact that a reader will be distracted by the readable content of a page when looking at its layout.</p></div>

  <div class="abs feature-photo" style="left:564px;top:389px;background:radial-gradient(circle at 50% 35%,#d8d0c0,#4a5277 35%,#1a1d33 80%)" role="img" aria-label="Photo of a person holding up a glowing light bulb under a starry sky"></div>
  <div class="abs feature" style="left:714px;top:395px"><h3>LOREM IPSUM IS SIMPLY</h3><p>It is a long established fact that a reader will be distracted by the readable content of a page when looking at its layout.</p></div>
</section>

<section class="slide s-closing">
  <div class="abs closing-photo" role="img" aria-label="Photo of a hand holding a light bulb with a glowing brain inside"></div>
  <h2 class="abs closing-title">IT IS A LONG ESTABLISHED<br>FACT THAT A READER WILL<br>BE DISTRACTED</h2>
  <p class="abs closing-text">There are many variations of passages of Lorem Ipsum available, but the majority have suffered alteration in some form, by injected humour, or randomised words which don't look even slightly believable. If you are going to use a passage of Lorem Ipsum, you need to be sure there isn't anything embarrassing hidden in the middle of text.</p>
  <div class="abs brand"><span>MindHarbor</span><span class="dot"></span></div>
</section>

</body>
</html>
```